Lighting, Light Bulbs Fluorescent, LED's, Ballast batteries, Exit Signs, Exit lights, Menu Boards, and Len's. Sales and repair services. For store and parking lots. Licensed and insured.

Store

```html
<!DOCTYPE html>
<html lang="en">
<head>
<meta charset="utf-8">
<title>Lighting Sales &amp; Service Postcard</title>
<link rel="stylesheet" href="https://fonts.googleapis.com/css2?family=Archivo+Black&family=Open+Sans:wght@400;600;700;800&display=swap">
<style>
  :root {
    --page-bg: #e9e9e9;
    --card-bg: #ffffff;
    --panel-grey: #eeeeee;
    --brand-green: #2e9b3e;
    --brand-red: #e3141b;
    --ink: #111111;
    --charcoal: #3a3a3a;
    --charcoal-dark: #2a2a2a;
  }
  * { margin: 0; padding: 0; box-sizing: border-box; }
  html, body { width: 900px; height: 1200px; overflow: hidden; }
  body {
    background: var(--page-bg);
    font-family: "Open Sans", Arial, sans-serif;
    position: relative;
  }
  .postcard {
    position: absolute;
    left: 90px;
    width: 720px;
    height: 525px;
    background: var(--card-bg);
    overflow: hidden;
    box-shadow: 0 4px 14px rgba(0,0,0,.18);
  }
  .postcard--front { top: 45px; background: linear-gradient(180deg, #ffffff 0%, var(--panel-grey) 100%); }
  .postcard--back { top: 630px; }
  .shapes { position: absolute; inset: 0; width: 100%; height: 100%; }

  /* Front */
  .badge {
    position: absolute; left: 216px; top: 40px;
    width: 124px; height: 124px; border-radius: 50%;
    background: var(--card-bg);
    border: 7px solid var(--brand-green);
    display: flex; align-items: center; justify-content: center; gap: 3px;
  }
  .badge__number {
    font-family: "Archivo Black", Arial, sans-serif;
    font-size: 36px; color: var(--brand-red); line-height: 1;
  }
  .badge__words {
    font-weight: 800; font-size: 11px; line-height: 1.1; color: var(--ink);
    text-transform: uppercase;
  }
  .headline {
    position: absolute; left: 428px; top: 62px; width: 282px;
    text-align: center; font-family: "Archivo Black", Arial, sans-serif;
    text-transform: uppercase; line-height: 1;
  }
  .headline__always { display: block; font-size: 48px; color: var(--ink); }
  .headline__free { display: block; font-size: 90px; color: var(--brand-red); margin-top: 2px; }
  .headline__delivery { display: block; font-size: 29px; color: var(--ink); margin-top: 8px; }
  .phone-bar {
    position: absolute; left: 400px; top: 405px; width: 320px; height: 58px;
    background: var(--charcoal); border-radius: 29px 0 0 29px;
    display: flex; align-items: center; padding-left: 12px; gap: 16px;
  }
  .phone-bar__icon {
    width: 38px; height: 38px; border-radius: 50%;
    background: #555; display: flex; align-items: center; justify-content: center;
  }
  .phone-bar__number {
    font-weight: 700; font-size: 30px; color: #fff; letter-spacing: 1px;
  }

  /* Back */
  .services {
    position: absolute; left: 16px; top: 238px; width: 300px;
  }
  .services__title {
    font-weight: 800; font-size: 17px; color: var(--brand-green);
    text-transform: uppercase; margin-bottom: 6px;
  }
  .services__list {
    list-style: none; display: grid; grid-template-columns: 168px 130px;
    row-gap: 3px; font-size: 14px; color: var(--ink);
  }
  .services__list li::before {
    content: "\2022"; color: var(--brand-green); margin-right: 3px;
  }
  .contact-strip {
    position: absolute; left: 0; top: 420px; width: 336px; height: 76px;
    background: var(--charcoal-dark);
    display: flex; justify-content: space-between; align-items: center;
    padding: 0 30px 0 34px; color: #e6e6e6; font-size: 11px; line-height: 1.55;
  }
  .contact-strip__address { font-style: normal; }
</style>
</head>
<body>

<section class="postcard postcard--front" aria-label="Postcard front">
  <svg class="shapes" viewBox="0 0 720 525" aria-hidden="true">
    <defs>
      <radialGradient id="bulbGlow" cx="0.42" cy="0.45" r="0.7">
        <stop offset="0" stop-color="#fff6d8"/>
        <stop offset="0.25" stop-color="#e8a56a"/>
        <stop offset="0.65" stop-color="#9a4a22"/>
        <stop offset="1" stop-color="#3a1206"/>
      </radialGradient>
    </defs>
    <polygon points="0,0 372,0 372,8 430,525 0,525" fill="var(--brand-green)"/>
    <polygon points="0,0 352,0 408,525 0,525" fill="var(--card-bg)"/>
    <polygon points="0,0 338,0 392,525 0,525" fill="url(#bulbGlow)" role="img" aria-label="Photo of a glowing fluorescent bulb held in cupped hands"/>
    <polygon points="392,525 720,470 720,525" fill="var(--brand-green)"/>
  </svg>

  <div class="badge">
    <span class="badge__number">30</span>
    <span class="badge__words">Over<br>Years</span>
  </div>

  <h1 class="headline">
    <span class="headline__always">Always</span>
    <span class="headline__free">Free</span>
    <span class="headline__delivery">Fast Delivery</span>
  </h1>

  <div class="phone-bar">
    <span class="phone-bar__icon">
      <svg width="20" height="20" viewBox="0 0 24 24" aria-hidden="true">
        <path fill="#fff" d="M6.6 10.8a15.1 15.1 0 0 0 6.6 6.6l2.2-2.2a1 1 0 0 1 1-.25 11.4 11.4 0 0 0 3.6.57 1 1 0 0 1 1 1V20a1 1 0 0 1-1 1A17 17 0 0 1 3 4a1 1 0 0 1 1-1h3.5a1 1 0 0 1 1 1c0 1.25.2 2.45.57 3.57a1 1 0 0 1-.25 1z"/>
      </svg>
    </span>
    <span class="phone-bar__number">555-014-2290</span>
  </div>
</section>

<section class="postcard postcard--back" aria-label="Postcard back">
  <svg class="shapes" viewBox="0 0 720 525" aria-hidden="true">
    <defs>
      <linearGradient id="ledPhoto" x1="0" y1="0" x2="1" y2="1">
        <stop offset="0" stop-color="#2f6fb8"/>
        <stop offset="0.5" stop-color="#c9d4dc"/>
        <stop offset="1" stop-color="#1d4f8a"/>
      </linearGradient>
    </defs>
    <polygon points="300,0 328,0 358,525 342,525" fill="var(--brand-green)"/>
    <polygon points="0,0 305,0 318,228 0,228" fill="url(#ledPhoto)" role="img" aria-label="Photo of an LED bulb held between fingers"/>
  </svg>

  <div class="services">
    <h2 class="services__title">Our Service</h2>
    <ul class="services__list">
      <li>Lighting</li><li>Exit lights</li>
      <li>Light Bulbs Fluorescent</li><li>Menu Boards</li>
      <li>LED's</li><li>Len's Sales</li>
      <li>Ballast batteries</li><li>repair services</li>
      <li>Exit Signs</li>
    </ul>
  </div>

  <div class="contact-strip">
    <address class="contact-strip__address">412 Cedar Mill Road<br>Brookdale, Georgia 30099</address>
    <p>555-014-2290<br>555-014-2291 Fax</p>
  </div>
</section>

</body>
</html>
```